Velmora Grove Club Postcard Design

Need a postcard for this business. Go to velmoragroveclub.com to see the product we are selling. Here's another good postcard you can sample. https://www.rowanpilsbydesign.com/?lightbox=dataItem-qz4tunal
Another one: http://blog.tranquet.com/postcard-examples-from-popular-startups/

```html
<!DOCTYPE html>
<html lang="en">
<head>
<meta charset="utf-8">
<title>Velmora Grove Club Postcard</title>
<link href="https://fonts.googleapis.com/css2?family=Montserrat:wght@400;500;700;800;900&family=Kurale&display=swap" rel="stylesheet">
<style>
  :root {
    --stage: #e4e4e4;
    --paper: #ffffff;
    --green-deep: #3a8a16;
    --green-bright: #86c82c;
    --brown-dark: #7d4b33;
    --brown-mid: #b56d58;
    --brown-text: #7a4632;
    --blush: #f6d2c4;
    --pill: #333333;
    --white: #ffffff;
    --dog-light: #54392c;
    --dog-dark: #2b1e18;
  }
  * { box-sizing: border-box; margin: 0; padding: 0; }
  html, body { width: 849px; height: 1200px; overflow: hidden; }
  body {
    background: var(--stage);
    font-family: "Montserrat", sans-serif;
    position: relative;
  }
  .postcard {
    position: absolute;
    left: 0; top: 296px;
    width: 849px; height: 607px;
    background: var(--paper);
    overflow: hidden;
  }
  .postcard__art { position: absolute; inset: 0; }
  .brand {
    position: absolute; left: 42px; top: 60px;
    display: flex; align-items: center; gap: 12px;
  }
  .brand__dot {
    width: 26px; height: 26px; border-radius: 50%;
    background: var(--brown-text);
  }
  .brand__name {
    font-weight: 800; font-size: 19px; line-height: 1.15;
    color: var(--brown-text); width: 120px;
  }
  .headline {
    position: absolute; left: 215px; top: 36px;
    font-weight: 900; font-size: 74px; letter-spacing: -1px; line-height: 1.1;
    background: linear-gradient(90deg, var(--green-deep), var(--green-bright));
    -webkit-background-clip: text; background-clip: text; color: transparent;
  }
  .subhead {
    position: absolute; left: 217px; top: 114px;
    font-weight: 800; font-size: 24px; line-height: 31px;
    color: var(--brown-text);
  }
  .subhead__rule {
    position: absolute; left: 217px; top: 188px;
    width: 70px; height: 3px; background: var(--brown-mid);
    border-radius: 2px;
  }
  .photo-dog {
    position: absolute; left: 318px; top: 210px;
    width: 300px; height: 262px;
    border-radius: 46% 46% 18% 18% / 40% 40% 16% 16%;
    background: linear-gradient(160deg, var(--dog-light), var(--dog-dark));
  }
  .features {
    position: absolute; left: 44px; top: 246px;
    list-style: none;
  }
  .features__item {
    display: flex; align-items: center; gap: 14px;
    height: 37.5px;
    font-family: "Kurale", serif; font-size: 18px; color: var(--white);
  }
  .features__icon { width: 26px; height: 26px; flex: none; }
  .offer { position: absolute; left: 45px; top: 460px; color: var(--white); }
  .offer__title { font-weight: 800; font-size: 30px; color: var(--blush); line-height: 32px; }
  .offer__line { font-weight: 500; font-size: 15px; letter-spacing: .5px; margin-top: 4px; }
  .offer__save { font-weight: 500; font-size: 18px; letter-spacing: .5px; margin-top: 6px; }
  .offer__save strong { font-weight: 800; font-size: 22px; }
  .offer__code {
    display: inline-block; margin-top: 8px;
    border: 1px dotted var(--white);
    padding: 5px 8px; font-size: 14px; font-weight: 400;
  }
  .offer__code strong { font-weight: 800; }
  .badge {
    position: absolute; left: 505px; top: 516px;
    width: 260px; height: 56px; border-radius: 28px;
    background: var(--pill);
    box-shadow: 0 4px 8px rgba(0,0,0,.3);
    display: flex; align-items: center; justify-content: center;
  }
  .badge::before {
    content: ""; position: absolute; inset: 5px;
    border: 1px dashed rgba(255,255,255,.7); border-radius: 24px;
  }
  .badge__text { position: relative; font-weight: 800; font-size: 24px; color: var(--white); }
</style>
</head>
<body>
<main class="postcard">
  <svg class="postcard__art" viewBox="0 0 849 607" width="849" height="607">
    <defs>
      <linearGradient id="greenBand" x1="0" x2="1" y1="0" y2="0">
        <stop offset="0" stop-color="#3a8a16"/>
        <stop offset="1" stop-color="#86c82c"/>
      </linearGradient>
      <linearGradient id="brownBand" x1="0" x2="1" y1="0" y2="0">
        <stop offset="0" stop-color="#84513a"/>
        <stop offset=".45" stop-color="#b56d58"/>
        <stop offset="1" stop-color="#7a4830"/>
      </linearGradient>
      <radialGradient id="sticksTone" cx=".5" cy=".5" r=".6">
        <stop offset="0" stop-color="#d9b88e"/>
        <stop offset=".6" stop-color="#9a6338"/>
        <stop offset="1" stop-color="#6b3f22"/>
      </radialGradient>
    </defs>
    <path d="M0,232 C160,200 330,196 520,215 L560,470 L0,470 Z" fill="url(#greenBand)"/>
    <path d="M0,212 C160,186 330,184 520,200" fill="none" stroke="#a5694f" stroke-width="4"/>
    <circle cx="765" cy="262" r="252" fill="url(#sticksTone)" stroke="#8a573c" stroke-width="12"
            role="img" aria-label="Photo of a pile of natural bully sticks"/>
    <path d="M0,443 C250,420 520,440 849,505 L849,607 L0,607 Z" fill="url(#brownBand)"/>
    <path d="M600,470 C700,475 790,460 849,430" fill="none" stroke="#f6d2c4" stroke-width="10"/>
  </svg>

  <div class="brand">
    <span class="brand__dot"></span>
    <span class="brand__name">Velmora Grove Club</span>
  </div>

  <h1 class="headline">SAVE</h1>
  <p class="subhead">All Natural, Pet<br>Approved Bully Sticks</p>
  <span class="subhead__rule"></span>

  <div class="photo-dog" role="img" aria-label="Photo of a dark brown and white puppy lying down chewing a bully stick"></div>

  <ul class="features">
    <li class="features__item">
      <svg class="features__icon" viewBox="0 0 26 26"><path d="M3,22 L6,8 L9,18 L13,4 L17,18 L20,8 L23,22 Z" fill="#fff"/></svg>
      Grass-Fed Beef</li>
    <li class="features__item">
      <svg class="features__icon" viewBox="0 0 26 26"><circle cx="13" cy="10" r="8" fill="none" stroke="#fff" stroke-width="3"/><path d="M8,16 L6,25 L10,22 L13,25 L16,22 L20,25 L18,16" fill="#fff"/></svg>
      Premium Quality</li>
    <li class="features__item">
      <svg class="features__icon" viewBox="0 0 26 26"><path d="M5,4 C9,2 11,5 13,5 C15,5 17,2 21,4 C24,7 21,13 20,17 L18,25 L15,16 L13,15 L11,16 L8,25 L6,17 C5,13 2,7 5,4 Z" fill="#fff"/></svg>
      Ideal for Dental Health</li>
    <li class="features__item">
      <svg class="features__icon" viewBox="0 0 26 26"><rect x="4" y="9" width="11" height="15" rx="1" fill="#fff"/><rect x="14" y="4" width="9" height="20" rx="1" fill="none" stroke="#fff" stroke-width="2"/></svg>
      High in Protein</li>
    <li class="features__item">
      <svg class="features__icon" viewBox="0 0 26 26"><path d="M13,2 C16,8 20,12 20,16 A7,7 0 0 1 6,16 C6,12 10,8 13,2 Z" fill="#fff"/><rect x="3" y="22" width="20" height="3" rx="1" fill="#fff"/></svg>
      Low in Fat</li>
  </ul>

  <section class="offer">
    <h2 class="offer__title">SIGN UP</h2>
    <p class="offer__line">FOR A SUBSCRIPTION &amp;</p>
    <p class="offer__save"><strong>SAVE 50%</strong> ON YOUR FIRST MONTH</p>
    <p class="offer__code">USE CODE: <strong>VELMORAGROVE</strong></p>
  </section>

  <div class="badge"><span class="badge__text">100% Digestible</span></div>
</main>
</body>
</html>
```